Consulting company (stride-and-calm, previously stundenfeld bremen) needs design for a clear and fre

This website is to be made completely new with Worpreess / Divi. I am at the beginning and have no idea about the design. The design is the focus of this order. After the first website I would like to use the design and colors for all other design products for business, which will be placed here as well.
On the website the services, the team, references ... should be separate pages. Please see the attached document. A very important part is the blog and the categories should be visible in the desktop view, vie widgets.

The site should be clear, well-arranged, but still convey freshness and vitality.
Our company offers consulting and online trainings for the following topics:
- Digital paperless office
- process optimization, digitalization
- Remote working and productivity
- Remote leadership
- remote project management
- Time management 4. 0
- Focus on the essentials

We do this in the form of:
- Keynote Speaking
- Facilitating
- Presentation
- Workshops and trainings
- Online trainings

Our services are intended exclusively for companies.

What drives us?
We want to inspire our customers to work more green, lean digital and focus on the essentials. We are a team of three people who are digital nomads, but who also work offline on site.
I do have already webseites, but they are old, but give you an idea what we do: stundenfeld-bremen.example.de. and ms-clearfile.example.com.

One style of a web site I like is for example is that of "plenvika.example.com" Colors I thought so far, but I'm not sure, could be the color palette "quarry bloom" from canva.com or something similar to # f60b80a and # 39dfa7. But I am open for other suggestions.
I love simple and clear fonts. I like this contemporary style of sites, where you get most of the content on the mobile devices by scrolling.

Target Market(s)

midsize and large businesses, decision maker

Logo Text

Let's work Stride and Calm

Number of Pages Required

5+ page

Font styles to use
Sans Serif

Colors
e34297
00a990

Requirements
Must have
• the page should be clear and concise, much white with color accents like content blocks or headlines, responsive,
Nice to have
• I like interesting backgrounds, very discreet, perhaps white and gray or the color shades of pastel, the site should somehow fit to the photos, the logo I added is the old one, just to give you an idea
Should not have
• in no case too playful or loud

```html
<!DOCTYPE html>
<html lang="en">
<head>
<meta charset="utf-8">
<title>Stride and Calm – Consulting</title>
<link href="https://fonts.googleapis.com/css2?family=Lato:ital,wght@0,400;0,700;0,900;1,400&display=swap" rel="stylesheet">
<style>
:root{
  --magenta:#e0287f;
  --teal:#14997f;
  --purple:#9b3f8c;
  --ink:#2b2b2b;
  --text:#3a3a3a;
  --soft:#f3f3f3;
  --footer:#2c2c2c;
  --white:#ffffff;
}
*{box-sizing:border-box;margin:0;padding:0}
html,body{width:1200px;height:3715px;overflow:hidden}
body{position:relative;font-family:'Lato',sans-serif;color:var(--text);background:var(--white)}
.abs{position:absolute}
a{color:inherit;text-decoration:none}

/* top bar */
.topbar{left:0;top:0;width:1200px;height:65px;background:var(--soft)}
.social{display:flex;gap:14px}
.social span{width:14px;height:14px;border-radius:50%;background:var(--teal);display:block}
.topbar .social{position:absolute;left:75px;top:25px}
.contact{position:absolute;right:74px;top:21px;font-size:18px;color:var(--ink);display:flex;gap:16px;align-items:center}
.contact .sep{color:var(--magenta)}
.contact svg{margin-right:10px;vertical-align:-2px}

/* header */
.header{left:0;top:65px;width:1200px;height:111px}
.brand{position:absolute;left:75px;top:29px;display:flex;align-items:center;gap:12px;font-size:30px;color:var(--ink)}
.brand .dot{width:48px;height:48px;border-radius:50%;background:var(--teal)}
.nav{position:absolute;left:640px;top:43px;display:flex;font-size:14px;font-weight:700;color:var(--white)}
.nav a{padding:11px 18px;border-radius:20px;text-transform:uppercase}
.nav a.active{background:var(--teal);padding:11px 22px}

/* hero */
.hero-title{left:75px;top:318px;font-size:68px;font-weight:900;line-height:62px;color:var(--magenta)}
.hero-tag{left:75px;top:458px;font-size:34px;font-style:italic;color:var(--ink)}

/* headings */
.h2{font-size:34px;font-weight:900;line-height:40px;color:var(--ink);text-transform:uppercase}
.h2 .accent{color:var(--teal)}
.btn{display:inline-block;background:var(--magenta);color:var(--white);font-size:15px;font-weight:700;text-transform:uppercase;border-radius:26px;text-align:center}

/* welcome */
.welcome-h{left:75px;top:820px}
.welcome-p{left:75px;top:910px;width:640px;font-size:14px;line-height:27.8px;white-space:nowrap}
.welcome-btn{left:75px;top:1122px;width:165px;height:49px;line-height:49px}
.welcome-img{left:704px;top:826px;width:422px;height:345px;border-radius:46px;background:linear-gradient(135deg,#eef0f1,#c9c5c0 60%,#8d857b)}

/* services */
.services{left:0;top:1252px;width:1200px;height:757px;background:var(--soft)}
.services-h{position:absolute;width:100%;top:56px;text-align:center}
.service-label{position:absolute;width:220px;margin-left:-110px;text-align:center;font-size:17px;font-weight:700;line-height:23px;color:var(--ink)}

/* formats */
.formats-h{left:75px;top:2084px;font-size:32px;font-weight:900;line-height:40px;color:var(--white)}
.arrows{left:1078px;top:2110px}
.card{top:2194px;width:242px;height:215px;border-radius:30px;background:var(--white);box-shadow:0 3px 14px rgba(0,0,0,.12);text-align:center;padding-top:104px}
.card h3{font-size:18px;color:var(--teal);font-weight:700}
.card p{font-size:14px;line-height:24px;margin-top:8px;color:var(--text)}

/* drives */
.drives-img{left:94px;top:2502px;width:389px;height:339px;border-radius:10px;background:linear-gradient(160deg,#f1f1f3,#dcdde3 55%,#f3d3e4)}
.drives-h{left:548px;top:2545px}
.drives-p{left:548px;top:2634px;width:600px;font-size:14px;line-height:28px;white-space:nowrap}
.drives-btn{left:548px;top:2748px;width:166px;height:47px;line-height:47px}

/* blog & tweets */
.panel{top:2923px;width:510px;height:402px;border-radius:46px;background:var(--soft)}
.panel h2{position:absolute;left:29px;top:34px;font-size:28px;font-weight:900;color:var(--ink)}
.panel h2 .accent{color:var(--teal)}
.item{position:absolute;left:29px;width:470px;display:flex;gap:20px}
.thumb{width:163px;height:122px;border-radius:14px;flex:none}
.item h4{font-size:16px;line-height:22px;font-weight:700;color:var(--teal);text-transform:uppercase}
.item p{font-size:14px;line-height:25px;margin-top:6px;white-space:nowrap}
.tweet p{font-size:14px;line-height:25px;margin-top:0}
.tweet .link{color:var(--teal)}
.tweet .ago{color:var(--magenta);font-style:italic;font-size:13px}

/* footer */
.footer{left:0;top:3401px;width:1200px;height:314px;background:var(--footer);color:var(--white)}
.footer .brand{left:75px;top:50px;font-size:28px;color:var(--white)}
.footer .brand .dot{width:40px;height:40px;background:var(--white)}
.copy{position:absolute;left:75px;top:128px;font-size:12px;line-height:25px}
.footer .social{position:absolute;left:75px;top:200px}
.footer .social span{background:var(--white)}
.fcol{position:absolute;top:58px}
.fcol h5{font-size:17px;font-weight:700;text-transform:uppercase;margin-bottom:10px}
.fcol li{list-style:none;font-size:13px;line-height:31.6px}
.email-input{position:absolute;left:884px;top:99px;width:242px;height:41px;border:1px solid #cfcfcf;border-radius:21px;font-size:12px;line-height:39px;padding-left:20px;color:#e6e6e6}
.signup{position:absolute;left:1036px;top:152px;width:89px;height:39px;line-height:39px;font-size:13px}
</style>
</head>
<body>

<div class="abs topbar">
  <div class="social"><span></span><span></span><span></span><span></span></div>
  <div class="contact">
    <span><svg width="14" height="14" viewBox="0 0 24 24"><path fill="#e0287f" d="M6.6 10.8a15 15 0 0 0 6.6 6.6l2.2-2.2c.3-.3.7-.4 1-.2 1.1.4 2.3.6 3.6.6.6 0 1 .4 1 1V20c0 .6-.4 1-1 1A17 17 0 0 1 3 4c0-.6.4-1 1-1h3.5c.6 0 1 .4 1 1 0 1.3.2 2.5.6 3.6.1.3 0 .7-.2 1z"/></svg>+49 421 5550 27 14</span>
    <span class="sep">|</span>
    <span><svg width="16" height="13" viewBox="0 0 24 18"><path fill="#e0287f" d="M0 0h24v18H0z"/><path fill="none" stroke="#fff" stroke-width="2" d="M1 1l11 8 11-8"/></svg>info@stundenfeld-bremen.example.de</span>
  </div>
</div>

<div class="abs header">
  <svg class="abs" style="left:0;top:0" width="1200" height="111">
    <defs><linearGradient id="band" x1="0" x2="1" y1="0" y2="0"><stop offset="0" stop-color="#a8408e"/><stop offset="1" stop-color="#8e3f88"/></linearGradient></defs>
    <path d="M389 0H1200V111H353Z" fill="url(#band)"/>
  </svg>
  <div class="brand"><span class="dot"></span>Stride and Calm</div>
  <nav class="nav">
    <a class="active" href="#">Home</a><a href="#">About Us</a><a href="#">Services</a><a href="#">Blog</a><a href="#">Contact Us</a>
  </nav>
</div>

<svg class="abs" style="left:0;top:176px" width="1200" height="574">
  <defs>
    <linearGradient id="arc" x1="0" y1="0" x2="0" y2="1"><stop offset="0" stop-color="#8e3f88"/><stop offset=".55" stop-color="#5a6f8c"/><stop offset="1" stop-color="#12997f"/></linearGradient>
    <linearGradient id="photo" x1="0" y1="0" x2="1" y2="1"><stop offset="0" stop-color="#c8ccd0"/><stop offset=".5" stop-color="#e7e7e3"/><stop offset="1" stop-color="#9f968d"/></linearGradient>
  </defs>
  <path d="M600 0H1200V395Q1100 560 860 574H600Z" fill="url(#arc)"/>
  <path d="M0 0H760C1010 0 1150 180 1130 330C1110 470 990 574 850 574H0Z" fill="url(#photo)" role="img" aria-label="Photo of a consultant working at a laptop in a bright office"/>
</svg>
<div class="abs hero-title">STRIDE AND<br>CALM</div>
<div class="abs hero-tag">Let's work Stride and Calm</div>

<h2 class="abs h2 welcome-h">Welcome to<br><span class="accent">Stride and Calm</span></h2>
<p class="abs welcome-p">I am a digital change maker and efficiency trainer because organizing, constantly<br>improving work processes and IT have been my passions for over 15 years and I can<br>convey the topic of organizational optimization to a wide variety of people very well.<br>In every office, I quickly grasp the state of the workplaces, the way employees work, the<br>paper and electronic processes, and I also quickly identify potential for optimization.<br>But we can only develop optimal processes together and highly efficient processes in the<br>office are no longer conceivable today without using the digital possibilities.</p>
<a class="abs btn welcome-btn" href="#">Read More</a>
<div class="abs welcome-img" role="img" aria-label="Portrait photo of the consultant in an office corridor"></div>

<section class="abs services">
  <h2 class="h2 services-h">Our <span class="accent">Services</span></h2>
  <svg class="abs" style="left:0;top:0" width="1200" height="757">
    <g stroke="#333" stroke-width="5" fill="none">
      <path d="M200 208L460 297L721 216L1020 265"/>
      <path d="M274 241L342 450"/>
      <path d="M940 330L707 472"/>
      <path d="M715 498L871 462L938 492"/>
    </g>
    <g stroke="#fff" stroke-width="5">
      <circle cx="200" cy="208" r="79" fill="#7fae4c" role="img" aria-label="Photo of a green home office desk"/>
      <circle cx="460" cy="297" r="87" fill="#b9b3ad" role="img" aria-label="Photo of a leader presenting to a team"/>
      <circle cx="721" cy="216" r="87" fill="#a9a39b" role="img" aria-label="Photo of colleagues working together"/>
      <circle cx="1020" cy="265" r="87" fill="#7d9bc4" role="img" aria-label="Photo of two focused colleagues"/>
      <circle cx="363" cy="529" r="77" fill="#8e9296" role="img" aria-label="Photo of metal gears"/>
      <circle cx="627" cy="529" r="87" fill="#b58a8e" role="img" aria-label="Photo of a consultant on a headset"/>
      <circle cx="1011" cy="542" r="87" fill="#c29a7a" role="img" aria-label="Photo of a hand stopping falling dominoes"/>
    </g>
  </svg>
  <div class="service-label" style="left:200px;top:304px">Digital Paperless<br>Office</div>
  <div class="service-label" style="left:460px;top:405px">Remote<br>Leadership</div>
  <div class="service-label" style="left:721px;top:327px">Remote Working and<br>Productivity</div>
  <div class="service-label" style="left:1020px;top:373px">Focus on the<br>Essentials</div>
  <div class="service-label" style="left:363px;top:628px">Process Optimization<br>Digitalization</div>
  <div class="service-label" style="left:627px;top:628px">Time<br>Management 4. 0</div>
  <div class="service-label" style="left:1011px;top:644px">Remote Project<br>Management</div>
</section>

<svg class="abs" style="left:0;top:2009px" width="600" height="290">
  <path d="M0 0H581C520 170 320 270 0 283Z" fill="var(--teal)"/>
</svg>
<h2 class="abs formats-h">WE DO THIS IN THE<br>FORM OF</h2>
<svg class="abs arrows" width="50" height="26" viewBox="0 0 50 26">
  <path d="M12 3L3 13L12 23M38 3L47 13L38 23" stroke="#555" stroke-width="3" fill="none"/>
</svg>
<div class="abs card" style="left:75px"><h3>Keynote Speaking</h3><p>Nulla mollis magna a finibus<br>viverra netus.</p></div>
<div class="abs card" style="left:345px"><h3>Facilitating</h3><p>Nulla mollis magna a finibus<br>viverra netus.</p></div>
<div class="abs card" style="left:614px"><h3>Presentation</h3><p>Nulla mollis magna a finibus<br>viverra netus.</p></div>
<div class="abs card" style="left:884px"><h3>Online Trainings</h3><p>Nulla mollis magna a finibus<br>viverra netus.</p></div>

<div class="abs drives-img" role="img" aria-label="Illustration of a woman working at a computer desk with shelves and plants"></div>
<h2 class="abs h2 drives-h">What<br><span class="accent">Drives Us?</span></h2>
<p class="abs drives-p">We want to inspire our customers to work more green, lean digital and focus on the<br>essentials. We are a team of three people who are digital nomads,<br>but who also work offline on site.</p>
<a class="abs btn drives-btn" href="#">Read More</a>

<section class="abs panel" style="left:75px">
  <h2>BLOG <span class="accent">POSTS</span></h2>
  <div class="item" style="top:91px">
    <div class="thumb" style="background:linear-gradient(135deg,#5a4a3e,#c99a6a)" role="img" aria-label="Photo of a team meeting around a table"></div>
    <div><h4>Intentional Encounters<br>Instead of Meetings</h4><p>Meetings are the plague, right? In any<br>case, I don't know anyone who would<br>like to be invited to a meeting.</p></div>
  </div>
  <div class="item" style="top:246px">
    <div class="thumb" style="background:linear-gradient(135deg,#7f9a7a,#d9d5ce)" role="img" aria-label="Photo of a consultant at a laptop"></div>
    <div><h4>Intentional Encounters<br>Instead of Meetings</h4><p>Meetings are the plague, right? In any<br>case, I don't know anyone who would<br>like to be invited to a meeting.</p></div>
  </div>
</section>

<section class="abs panel" style="left:616px">
  <h2>LATEST <span class="accent">TWEETS</span></h2>
  <div class="item tweet" style="top:91px">
    <div class="thumb" style="background:linear-gradient(135deg,#e9e9e9,#8a7f7a)" role="img" aria-label="Profile photo of the consultant"></div>
    <div><p>@Time saving Meetings are the plague,<br>right? Exchange is better, because<br>digital transparency creates the prereq-<br>uisite for ... <span class="link">lnk.example.com/Tq7Mw2</span></p><p class="ago">6 months ago</p></div>
  </div>
  <div class="item tweet" style="top:246px">
    <div class="thumb" style="background:linear-gradient(135deg,#c89a84,#7b5a48)" role="img" aria-label="Close-up profile photo of the consultant"></div>
    <div><p>@Time saving Meetings are the plague,<br>right? Exchange is better, because<br>digital transparency creates the prereq-<br>uisite for ... <span class="link">lnk.example.com/Tq7Mw2</span></p><p class="ago">6 months ago</p></div>
  </div>
</section>

<footer class="abs footer">
  <div class="brand abs"><span class="dot"></span>Stride and Calm</div>
  <p class="copy">Copyright © 2020. Company Name.<br>All Right Reserved</p>
  <div class="social"><span></span><span></span><span></span><span></span></div>
  <div class="fcol" style="left:386px"><h5>Site Map</h5><ul><li>Home</li><li>About Us</li><li>Services</li><li>Blog</li><li>Contact Us</li></ul></div>
  <div class="fcol" style="left:593px"><h5>Services</h5><ul><li>Digital paperless office</li><li>Process optimization, digitalization</li><li>Remote working and productivity</li><li>Remote leadership</li><li>Remote project management</li><li>Time management 4. 0</li></ul></div>
  <div class="fcol" style="left:887px"><h5>Email Sign Up</h5></div>
  <div class="email-input">Enter Email Address</div>
  <a class="btn signup" href="#">Sign Up</a>
</footer>

</body>
</html>
```